Process Serving Company needs a letterhead design

Looking to have a letterhead designed for letters to attorneys advertising our business. We would like something eye catching but professional. Colors and logos are attached. Please add "Process Service and Attorney Support" near the logo or header

Target Market(s)

Attorneys

Font styles to use
Serif
Sans Serif

Colors
33a6d7
0255a3
85cae6
cee9f5
ecf7fb

```html
<!DOCTYPE html>
<html lang="en">
<head>
<meta charset="utf-8">
<title>Mesa Line Legal Courier – Letterhead</title>
<link rel="stylesheet" href="https://fonts.googleapis.com/css2?family=Open+Sans:wght@400;600&family=Roboto:wght@400&family=Montserrat:wght@500&display=swap">
<style>
  :root {
    --blue: #33a6d7;
    --blue-deep: #1290cf;
    --navy: #0255a3;
    --sky: #85cae6;
    --mist: #cee9f5;
    --ink: #3a3a3a;
    --ink-soft: #4a4a4a;
    --backdrop: #dedfe1;
    --paper-top: #ffffff;
    --paper-bottom: #f1f2f3;
  }
  * { box-sizing: border-box; margin: 0; padding: 0; }
  html, body { width: 1063px; height: 1200px; overflow: hidden; }
  body {
    background: var(--backdrop);
    font-family: "Open Sans", sans-serif;
    color: var(--ink);
    position: relative;
  }
  .letterhead {
    position: absolute;
    left: 96px; top: 30px;
    width: 871px; height: 1140px;
    background: linear-gradient(180deg, var(--paper-top) 0%, var(--paper-top) 35%, var(--paper-bottom) 100%);
    box-shadow: 0 6px 24px rgba(0,0,0,0.12);
  }
  .brand {
    position: absolute;
    left: 72px; top: 118px;
    display: flex; align-items: center; gap: 12px;
  }
  .brand-square {
    width: 34px; height: 34px;
    background: var(--blue-deep);
  }
  .brand-name {
    font-family: "Open Sans", sans-serif;
    font-weight: 600;
    font-size: 24px;
    color: var(--blue-deep);
    letter-spacing: 0.3px;
  }
  .contact {
    position: absolute;
    left: 560px; top: 64px;
    font-family: "Roboto", sans-serif;
    font-size: 13px;
    line-height: 18px;
    color: var(--ink);
  }
  .contact .address { margin-bottom: 2px; }
  .contact-row { display: flex; align-items: center; gap: 8px; padding-left: 8px; }
  .contact-row svg { width: 12px; height: 12px; fill: var(--blue-deep); flex: none; }
  .letter-body {
    position: absolute;
    left: 120px; top: 300px;
    width: 640px;
    font-size: 15px;
    line-height: 22px;
    color: var(--ink-soft);
  }
  .salutation { margin-bottom: 20px; }
  .letter-body p.para { margin-bottom: 22px; }
  .closing { margin-top: 10px; }
  .signature {
    display: block;
    margin: 26px 0 0 20px;
    width: 110px; height: 70px;
    background: linear-gradient(135deg, #f1f2f3, #e3e4e6);
    border-radius: 4px;
  }
  .footer-band {
    position: absolute;
    left: 0; right: 0; bottom: 0;
    height: 52px;
    background: var(--blue-deep);
    display: flex; align-items: center; justify-content: center;
    font-family: "Montserrat", sans-serif;
    font-weight: 500;
    font-size: 17px;
    letter-spacing: 0.6px;
    text-transform: uppercase;
    color: #ffffff;
  }
</style>
</head>
<body>
  <main class="letterhead">
    <div class="brand">
      <span class="brand-square"></span>
      <span class="brand-name">Mesa Line Legal Courier</span>
    </div>

    <address class="contact" style="font-style:normal">
      <div class="address">2150 E Canyon View Rd STE 40<br>Tempe AZ 85281</div>
      <div class="contact-row">
        <svg viewBox="0 0 24 24" aria-hidden="true"><path d="M6.6 10.8a15 15 0 0 0 6.6 6.6l2.2-2.2c.3-.3.7-.4 1-.2 1.1.4 2.3.6 3.6.6.6 0 1 .4 1 1V20c0 .6-.4 1-1 1A17 17 0 0 1 3 4c0-.6.4-1 1-1h3.5c.6 0 1 .4 1 1 0 1.3.2 2.5.6 3.6.1.3 0 .7-.2 1z"/></svg>
        <span>480-555-0142</span>
      </div>
      <div class="contact-row">
        <svg viewBox="0 0 24 24" aria-hidden="true"><path d="M6 2h12v5H6zM3 8h18a1 1 0 0 1 1 1v8h-4v5H6v-5H2V9a1 1 0 0 1 1-1zm5 8v4h8v-4z"/></svg>
        <span>480-555-0187</span>
      </div>
      <div class="contact-row">
        <svg viewBox="0 0 24 24" aria-hidden="true"><path d="M2 5h20v14H2zm2 2v.5l8 5 8-5V7z"/></svg>
        <span>Dana@MesaLineLegal.com</span>
      </div>
      <div class="contact-row">
        <svg viewBox="0 0 24 24" aria-hidden="true"><path d="M12 2a10 10 0 1 0 0 20 10 10 0 0 0 0-20zm0 2c.9 1.2 1.7 3 2 5h-4c.3-2 1.1-3.8 2-5zM4.3 9h3.7a17 17 0 0 0 0 6H4.3a8 8 0 0 1 0-6zm5.7 0h4a15 15 0 0 1 0 6h-4a15 15 0 0 1 0-6zm6 0h3.7a8 8 0 0 1 0 6H16a17 17 0 0 0 0-6zm-6 8h4c-.3 2-1.1 3.8-2 5-.9-1.2-1.7-3-2-5z"/></svg>
        <span>www.MesaLineLegal.com</span>
      </div>
    </address>

    <section class="letter-body">
      <p class="salutation">Dear customer,</p>
      <p class="para">Lorem ipsum dolor sit amet, consectetur adipisicing elit, sed do eiusmod tempor incididunt ut labore et dolore magna aliqua. Ut enim ad minim veniam, quis nostrud exercitation ullamco laboris nisi ut aliquip ex ea commodo consequat. Duis aute irure dolor in reprehenderit in voluptate velit esse cillum dolore eu fugiat nulla pariatur. Excepteur sint occaecat cupidatat non proident, sunt in culpa qui officia deserunt mollit anim id est laborum.</p>
      <p class="para">Lorem ipsum dolor sit amet, consectetur adipisicing elit, sed do eiusmod tempor incididunt ut labore et dolore magna aliqua. Ut enim ad minim veniam, quis nostrud exercitation ullamco laboris nisi ut aliquip ex ea commodo consequat. Duis aute irure dolor in reprehenderit in voluptate velit esse cillum dolore eu fugiat nulla pariatur. Excepteur sint occaecat cupidatat non proident, sunt in culpa qui officia deserunt mollit anim id est laborum.</p>
      <p class="para">Lorem ipsum dolor sit amet, consectetur adipisicing elit, sed do eiusmod tempor incididunt ut labore et dolore magna aliqua. Ut enim ad minim veniam, quis nostrud exercitation ullamco laboris nisi ut aliquip ex ea commodo consequat. Duis aute irure dolor in reprehenderit in voluptate velit esse cillum dolore eu fugiat nulla pariatur. Excepteur sint occaecat cupidatat non proident, sunt in culpa qui officia deserunt mollit anim id est laborum.</p>
      <p class="para">Lorem ipsum dolor sit amet, consectetur adipisicing elit, sed do eiusmod tempor incididunt ut labore et dolore magna aliqua. Ut enim ad minim veniam, quis nostrud exercitation ullamco laboris nisi ut aliquip ex ea commodo consequat. Duis aute irure dolor in reprehenderit.</p>
      <p class="closing">Yours Sincerely,</p>
      <span class="signature" role="img" aria-label="Handwritten signature of the sender"></span>
    </section>

    <footer class="footer-band">Process Service and Attorney Support</footer>
  </main>
</body>
</html>
```